Kickass business card and letter head needed!
Web Hosting company Business Card
Modern
Gordon Pell
Director
PO Box 903 Walled Lake, MI 48390
gpell@brightkeelhosting.example
http://www.brightkeel.example
Hosting over 50,000 web sites In business since 1999 Family owned and operated
Web Hosting * Dedicated Servers * Co-location Services * Unix, Linux and Window Administration Services * Secure Data Retention * Virtual Private Servers * Web Design and SEO Services * Reseller Hosting * Cloud Hosting *

```html
<!DOCTYPE html>
<html lang="en">
<head>
<meta charset="utf-8">
<title>brightkeel hosting stationery</title>
<link rel="stylesheet" href="https://fonts.googleapis.com/css2?family=Roboto:wght@400;700;900&display=swap">
<style>
:root{
  --bg:#d9d9d9;
  --paper:#ffffff;
  --ink:#1a1a1a;
  --black:#111111;
  --grey:#8a8a8a;
  --light-grey:#bbbbbb;
  --faint:#eeeeee;
  --shadow:rgba(0,0,0,.18);
}
*{box-sizing:border-box;margin:0;padding:0}
html,body{width:1200px;height:578px;overflow:hidden}
body{background:var(--bg);font-family:"Roboto",Arial,sans-serif;color:var(--ink);position:relative}
.sheet{position:absolute;background:var(--paper);box-shadow:0 2px 6px var(--shadow);overflow:hidden}
.wordmark{font-weight:900;letter-spacing:-.5px;line-height:1;white-space:nowrap}
.tagline{font-size:4px;color:var(--grey);letter-spacing:.5px;text-transform:uppercase;white-space:nowrap}
.fine{font-size:5px;line-height:7px;color:var(--grey);white-space:nowrap}

/* business cards */
.card{left:20px;width:220px;height:92px}
.card--dark{background:var(--black);color:var(--paper)}
.card .wordmark{position:absolute;right:14px;top:14px;font-size:17px}
.card .tagline{position:absolute;right:14px;top:33px}
.card__person{position:absolute;left:12px;top:12px}
.card__name{font-size:7px;font-weight:700;color:var(--ink)}
.card--dark .card__name{color:var(--paper)}
.card__role{font-size:5px;color:var(--grey)}
.card__lists{position:absolute;left:12px;bottom:10px;display:flex;gap:18px}
.card__lists ul{list-style:none}
.card--dark .fine{color:var(--light-grey)}
.card__contact{position:absolute;right:14px;bottom:10px;text-align:right}

/* letterheads */
.letter{top:38px;width:300px;height:500px}
.letter__head .wordmark{position:absolute;left:22px;top:22px;font-size:22px}
.letter__head .tagline{position:absolute;left:22px;top:46px}
.letter__watermark{position:absolute;left:0;right:0;top:190px;text-align:center;font-size:54px;color:var(--faint)}
.letter__foot{position:absolute;left:22px;bottom:22px;display:flex;gap:24px}
.letter--band .letter__band{position:absolute;left:0;right:0;top:0;height:34px;background:var(--black)}
.letter--band .letter__head .wordmark{color:var(--paper);top:8px;font-size:18px}
.letter--band .letter__contact{position:absolute;right:20px;top:44px;text-align:right}

/* envelopes */
.envelope{left:900px;width:280px;height:140px}
.envelope .wordmark{position:absolute;left:18px;top:16px;font-size:16px}
.envelope .tagline{position:absolute;left:18px;top:34px}
.envelope__return{position:absolute;left:18px;top:44px}
.envelope__band{position:absolute;left:0;top:12px;width:110px;height:30px;background:var(--black)}
.envelope--band .wordmark{color:var(--paper);top:19px}
.envelope--band .tagline{top:48px}
.envelope--band .envelope__return{top:58px}
.envelope__flap{position:absolute;inset:0}
</style>
</head>
<body>

<!-- business cards -->
<section class="sheet card" style="top:38px">
  <div class="card__person"><p class="card__name">Gordon Pell</p><p class="card__role">Director</p></div>
  <p class="wordmark">brightkeel</p>
  <p class="tagline">Web Hosting</p>
  <div class="card__contact fine"><p>PO Box 903 Walled Lake, MI 48390</p><p>gpell@brightkeelhosting.example</p><p>http://www.brightkeel.example</p></div>
</section>

<section class="sheet card" style="top:146px">
  <p class="wordmark">brightkeel</p>
  <p class="tagline">Web Hosting</p>
  <div class="card__lists fine">
    <ul><li>Web Hosting</li><li>Dedicated Servers</li><li>Co-location Services</li><li>Cloud Hosting</li></ul>
    <ul><li>Virtual Private Servers</li><li>Secure Data Retention</li><li>Web Design and SEO</li><li>Reseller Hosting</li></ul>
  </div>
</section>

<section class="sheet card card--dark" style="top:254px">
  <div class="card__person"><p class="card__name">Gordon Pell</p><p class="card__role">Director</p></div>
  <p class="wordmark">brightkeel</p>
  <p class="tagline">Web Hosting</p>
  <div class="card__contact fine"><p>PO Box 903 Walled Lake, MI 48390</p><p>gpell@brightkeelhosting.example</p><p>http://www.brightkeel.example</p></div>
</section>

<section class="sheet card card--dark" style="top:362px">
  <p class="wordmark">brightkeel</p>
  <p class="tagline">Web Hosting</p>
  <div class="card__lists fine">
    <ul><li>Hosting over 50,000 web sites</li><li>In business since 1999</li><li>Family owned and operated</li></ul>
    <ul><li>Unix, Linux and Window</li><li>Administration Services</li><li>Secure Data Retention</li></ul>
  </div>
</section>

<!-- letterhead, white -->
<section class="sheet letter" style="left:260px">
  <div class="letter__head"><p class="wordmark">brightkeel</p><p class="tagline">Web Hosting</p></div>
  <p class="letter__watermark wordmark" aria-hidden="true">brightkeel</p>
  <div class="letter__foot fine">
    <div><p>PO Box 903</p><p>Walled Lake, MI 48390</p></div>
    <div><p>T (248) 555-0142</p><p>F (248) 555-0187</p></div>
    <div><p>gpell@brightkeelhosting.example</p><p>http://www.brightkeel.example</p></div>
  </div>
</section>

<!-- letterhead, black band -->
<section class="sheet letter letter--band" style="left:580px">
  <div class="letter__band"></div>
  <div class="letter__head"><p class="wordmark">brightkeel</p></div>
  <div class="letter__contact fine">
    <p>PO Box 903 Walled Lake, MI 48390</p><p>T (248) 555-0142 &middot; F (248) 555-0187</p><p>http://www.brightkeel.example</p>
  </div>
  <p class="letter__watermark wordmark" aria-hidden="true">brightkeel</p>
</section>

<!-- envelopes -->
<section class="sheet envelope" style="top:38px">
  <p class="wordmark">brightkeel</p>
  <p class="tagline">Web Hosting</p>
  <div class="envelope__return fine"><p>PO Box 903</p><p>Walled Lake, MI 48390</p></div>
</section>

<section class="sheet envelope envelope--band" style="top:218px">
  <div class="envelope__band"></div>
  <p class="wordmark">brightkeel</p>
  <p class="tagline">Web Hosting</p>
  <div class="envelope__return fine"><p>PO Box 903</p><p>Walled Lake, MI 48390</p></div>
</section>

<section class="sheet envelope" style="top:398px">
  <svg class="envelope__flap" viewBox="0 0 280 140" aria-hidden="true">
    <path d="M0 0 H280 L160 62 Q140 72 120 62 Z" fill="#111111"/>
    <path d="M0 0 L120 62 Q140 72 160 62 L280 0" fill="none" stroke="#cfcfcf" stroke-width="1"/>
    <circle cx="140" cy="40" r="5" fill="#ffffff"/>
  </svg>
</section>

</body>
</html>
```